依頼詳細
味付け海苔は、添付しました写真のような袋に入っており、そこに帯を巻くような形でパッケージしようと考えております。現在その帯に和紙風の紙を使用しようと考案中です。
■ パッケージデザインへの要望

・瀬戸内牛窓産
・澄風庵“こはる”
のキーワードが入り、高級感があるデザイン

■ 商品情報

小袋6枚入り×32袋の味付け海苔

■ パッケージの情報
今回はZIP付きのビニール
サイズ:W185mm × H380mm

上記の袋にH210mmの帯を中央に巻く(幅はビニールの幅と同様)

```html
<!DOCTYPE html>
<html lang="ja">
<head>
<meta charset="UTF-8">
<title>澄風庵 こはる 味付けのり 帯</title>
<link rel="stylesheet" href="https://fonts.googleapis.com/css2?family=Shippori+Mincho:wght@500;700;800&family=Yuji+Syuku&display=swap">
<style>
  :root{
    --paper:#ffffff;
    --bag:#dcdcdc;
    --trim:#9a9a9a;
    --kraft:#a77f3f;
    --kraft-light:#b8924f;
    --kraft-dark:#8e6a34;
    --enso:#7a5a2a;
    --ink:#1b1208;
    --copy:#2a1a08;
    --black:#0e0e0e;
    --slate:#4a4a4a;
    --slate-dark:#2e2e2e;
    --cream:#e9e1cc;
    --silver:#d2d2d2;
    --muted:#9c9c9c;
    --seal:#b3241d;
  }
  *{margin:0;padding:0;box-sizing:border-box}
  html,body{width:1200px;height:2308px;overflow:hidden;background:var(--paper)}
  .canvas{position:relative;width:1200px;height:2308px}
  .crop-marks{position:absolute;inset:0}
  .bag{position:absolute;left:72px;top:72px;width:1056px;height:2168px;background:var(--bag)}
  .band{position:absolute;left:72px;top:550px;width:1056px;height:1208px}
  .band-kraft{position:absolute;left:0;top:0;width:640px;height:100%;overflow:hidden;
    background:linear-gradient(165deg,var(--kraft-light),var(--kraft) 50%,var(--kraft-dark))}
  .enso{position:absolute;left:208px;top:330px;width:480px;height:480px;border-radius:50%;
    background:radial-gradient(circle,rgba(122,90,42,.25) 0%,rgba(122,90,42,.45) 70%,rgba(122,90,42,.1) 100%)}
  .band-black{position:absolute;left:640px;top:0;width:416px;height:100%;background:var(--black)}
  .slate-panel{position:absolute;left:640px;top:100px;width:416px;height:840px;
    background:radial-gradient(ellipse at 40% 30%,var(--slate),var(--slate-dark) 80%)}
  .vert{position:absolute;writing-mode:vertical-rl;white-space:nowrap}
  .product-name{left:410px;top:300px;font-family:"Yuji Syuku",serif;font-size:172px;line-height:1;color:var(--ink);letter-spacing:2px}
  .copy{font-family:"Shippori Mincho",serif;font-weight:800;font-size:36px;line-height:1;color:var(--copy);letter-spacing:0}
  .copy-1{left:344px;top:440px}
  .copy-2{left:272px;top:500px}
  .copy-3{left:200px;top:520px}
  .contents{position:absolute;left:228px;top:945px;font-family:"Shippori Mincho",serif;font-weight:500;font-size:28px;color:var(--copy);white-space:nowrap}
  .category{left:684px;top:290px;font-family:"Shippori Mincho",serif;font-weight:700;font-size:52px;line-height:1;color:var(--cream);letter-spacing:2px}
  .origin{left:752px;top:470px;font-family:"Shippori Mincho",serif;font-weight:500;font-size:30px;line-height:1;color:var(--muted);letter-spacing:2px}
  .origin::before,.origin::after{content:"";display:inline-block;width:1px;height:60px;background:var(--muted);margin:12px 0}
  .brand{left:850px;top:330px;font-family:"Shippori Mincho",serif;font-weight:500;font-size:168px;line-height:1;color:var(--silver);letter-spacing:4px}
  .seal{position:absolute;left:970px;top:860px;width:44px;height:44px;background:var(--seal)}
</style>
</head>
<body>
<div class="canvas">
  <div class="bag"></div>

  <div class="band">
    <div class="band-kraft" role="img" aria-label="和紙風の質感の帯">
      <div class="enso" role="img" aria-label="筆で描いた円の墨模様"></div>
    </div>
    <div class="band-black"></div>
    <div class="slate-panel"></div>

    <div class="vert product-name">こはる</div>
    <div class="vert copy copy-1">パリっとした食感に</div>
    <div class="vert copy copy-2">仕上がりました</div>
    <div class="vert copy copy-3">ご飯のお供に最適です。</div>
    <div class="contents">小袋6枚入り×32袋</div>

    <div class="vert category">味付けのり</div>
    <div class="vert origin">瀬戸内牛窓産</div>
    <div class="vert brand">澄風庵</div>
    <div class="seal"></div>
  </div>

  <svg class="crop-marks" width="1200" height="2308" viewBox="0 0 1200 2308" stroke="var(--trim)" stroke-width="2" fill="none">
    <path d="M0 72H52M72 0V52M0 60H52M60 0V52"/>
    <path d="M1148 72H1200M1128 0V52M1148 60H1200M1140 0V52"/>
    <path d="M0 2240H52M72 2256V2308M0 2248H52M60 2256V2308"/>
    <path d="M1148 2240H1200M1128 2256V2308M1148 2248H1200M1140 2256V2308"/>
    <path d="M0 1154H52M1148 1154H1200M600 0V52M600 2256V2308"/>
  </svg>
</div>
</body>
</html>
```